Local Horticulturalist needs Business card design

Meridel Horticulture would like to update our existing business card and utilize our new logo (design attached)....we specialize in getting the best out of our customers yard with professional maintenance programs, expert pruning and hedging and garden restorations.
Utilizing colors from attached logo I would like a design that implies professionalism and if possible our businesses love of restoration through plants.
I also sometimes write down for my customers a start date and price on the back of my current card
Target Market(s)
Home owners
Contractors
Industry/Entity Type
Gardener
Contact Information for Business Card
Gareth Volkstrom | Horticulturalist
ph: 0438275946
meridelhort@fernmail.example
www.meridelhorticulture.example.au
Requirements
Must have
- crucial information easy to read
- incorporate current logo
- Horticulturalist listed preferably near name
Nice to have
- currently I write a job start date and price on the back of my current card so something that integrates this would be beneficial
Should not have
- be pretty or flowerey
- be too white or basic

```html
<!DOCTYPE html>
<html lang="en">
<head>
<meta charset="utf-8">
<title>Meridel Horticulture – Business Card</title>
<link href="https://fonts.googleapis.com/css2?family=Cabin:wght@400;600;700&display=swap" rel="stylesheet">
<style>
  :root {
    --leaf-green: #7cb83a;
    --pale-green: #d9ecc1;
    --soil-brown: #6b5a45;
    --card-white: #ffffff;
    --backdrop: #ecece8;
  }
  * { box-sizing: border-box; margin: 0; padding: 0; }
  html, body { width: 1200px; height: 800px; overflow: hidden; }
  body {
    background: var(--backdrop);
    font-family: "Cabin", "Gill Sans", sans-serif;
    display: flex;
    align-items: center;
    justify-content: center;
    gap: 40px;
  }
  .card {
    position: relative;
    width: 540px;
    height: 330px;
    background: var(--card-white);
    box-shadow: 0 6px 18px rgba(0,0,0,0.12);
    overflow: hidden;
  }

  /* Front */
  .card-front .band {
    position: absolute; left: 0; right: 0; height: 48px;
    background: var(--pale-green);
  }
  .card-front .band-top { top: 0; }
  .card-front .band-bottom { bottom: 0; }
  .card-front .brand {
    position: absolute; top: 50%; left: 50%;
    transform: translate(-50%, -50%);
    display: flex; align-items: center; gap: 14px;
    white-space: nowrap;
  }
  .brand-dot {
    width: 46px; height: 46px; border-radius: 50%;
    background: var(--leaf-green);
    flex: none;
  }
  .brand-name {
    color: var(--leaf-green);
    font-weight: 700;
    font-size: 30px;
  }

  /* Back */
  .card-back .brand-panel {
    position: absolute; left: 0; top: 0; bottom: 0; width: 200px;
    background: var(--card-white);
    display: flex; flex-direction: column; align-items: center; justify-content: center;
    gap: 14px;
  }
  .card-back .brand-panel .brand-dot { width: 78px; height: 78px; }
  .card-back .brand-panel .brand-name { font-size: 16px; }
  .info-panel {
    position: absolute; left: 200px; right: 0; top: 0; bottom: 0;
    background: var(--pale-green);
  }
  .person {
    position: absolute; top: 36px; left: 20px; width: 270px;
    text-align: center;
  }
  .person-name {
    color: var(--leaf-green);
    font-weight: 600; font-size: 21px; letter-spacing: 1.2px;
    text-transform: uppercase;
  }
  .person-role {
    display: flex; align-items: center; gap: 6px;
    color: var(--soil-brown); font-size: 9px; letter-spacing: 1px;
    text-transform: uppercase; margin-top: 2px;
  }
  .person-role::before, .person-role::after {
    content: ""; flex: 1; height: 1px; background: var(--soil-brown);
  }
  .contact {
    list-style: none; margin-top: 10px;
    color: var(--leaf-green); font-weight: 600; font-size: 12px; line-height: 1.35;
  }
  .write-field { position: absolute; }
  .write-field .field-label {
    display: block; color: var(--soil-brown);
    font-size: 9px; font-weight: 600; letter-spacing: 0.6px;
    text-transform: uppercase; margin-bottom: 2px;
  }
  .write-field .field-box {
    display: block; width: 88px; height: 24px;
    background: var(--card-white);
    border: 2px solid var(--leaf-green);
  }
  .field-price { right: 26px; top: 150px; }
  .field-price .field-label { text-align: left; padding-left: 14px; }
  .field-start { left: 26px; top: 238px; }
</style>
</head>
<body>
  <section class="card card-front" aria-label="Card front">
    <div class="band band-top"></div>
    <div class="brand">
      <span class="brand-dot"></span>
      <span class="brand-name">Meridel Horticulture</span>
    </div>
    <div class="band band-bottom"></div>
  </section>

  <section class="card card-back" aria-label="Card back">
    <div class="brand-panel">
      <span class="brand-dot"></span>
      <span class="brand-name">Meridel Horticulture</span>
    </div>
    <div class="info-panel">
      <div class="person">
        <h1 class="person-name">Gareth Volkstrom</h1>
        <p class="person-role">Horticulturalist</p>
        <ul class="contact">
          <li>0438 275 946</li>
          <li>meridelhort@fernmail.example</li>
          <li>meridelhorticulture.example.au</li>
        </ul>
      </div>
      <div class="write-field field-price">
        <span class="field-label">Price</span>
        <span class="field-box"></span>
      </div>
      <div class="write-field field-start">
        <span class="field-label">Start Date</span>
        <span class="field-box"></span>
      </div>
    </div>
  </section>
</body>
</html>
```